Ned Farrow & Alan Brisbourne Two Piano Recital

We need a flyer designed to advertise a classical concert featuring pianists Alan Brisbourne & Ned Farrow playing two pianos.

The concert will be held at Kelwood College on Thursday, June 12th at 7:30pm
Supper will be served!
We need something that will get noticed and look cool possibly using the photo attached?

```html
<!DOCTYPE html>
<html lang="en">
<head>
<meta charset="utf-8">
<title>Alan Brisbourne &amp; Ned Farrow – Two Piano Recital</title>
<link rel="stylesheet" href="https://fonts.googleapis.com/css2?family=Josefin+Sans:wght@300;400&family=Questrial&family=Open+Sans:wght@400&display=swap">
<style>
  :root {
    --paper: #ffffff;
    --ink: #000000;
    --photo-light: #8a8a8a;
    --photo-mid: #4a4a4a;
    --photo-dark: #141414;
    --gold-edge: #d98a1c;
    --gold-mid: #e9c45a;
    --gold-light: #f4ef9c;
    --band-text: #2a2216;
    --name-white: #ffffff;
    --red: #ee2a0c;
  }
  html, body {
    margin: 0;
    padding: 0;
    width: 880px;
    height: 1200px;
    overflow: hidden;
    background: var(--paper);
  }
  .flyer {
    position: absolute;
    left: 36px;
    top: 36px;
    width: 806px;
    height: 1126px;
    background: var(--ink);
    overflow: hidden;
  }
  .performer-photo {
    position: absolute;
    left: 0;
    top: 0;
    width: 100%;
    height: 1040px;
    background:
      linear-gradient(180deg, rgba(0,0,0,0) 0%, rgba(0,0,0,0) 55%, rgba(0,0,0,0.55) 78%, var(--ink) 100%),
      linear-gradient(90deg, var(--photo-dark) 0%, var(--photo-mid) 22%, var(--photo-light) 48%, var(--photo-mid) 72%, var(--photo-dark) 100%);
  }
  .tagline-band {
    position: absolute;
    left: 0;
    top: 600px;
    width: 100%;
    height: 96px;
    background: linear-gradient(90deg, var(--gold-edge) 0%, var(--gold-mid) 25%, var(--gold-light) 50%, var(--gold-mid) 75%, var(--gold-edge) 100%);
    display: flex;
    align-items: center;
    justify-content: center;
  }
  .tagline {
    margin: 0;
    font-family: "Questrial", sans-serif;
    font-size: 44px;
    font-weight: 400;
    color: var(--band-text);
    letter-spacing: -0.5px;
  }
  .performers {
    position: absolute;
    left: 0;
    top: 730px;
    width: 100%;
    text-align: center;
    font-family: "Josefin Sans", sans-serif;
    font-weight: 300;
    color: var(--name-white);
    text-transform: uppercase;
    text-shadow: 0 2px 6px rgba(0,0,0,0.6);
  }
  .performer {
    margin: 0;
    font-weight: 300;
    line-height: 1;
  }
  .performer-first {
    font-size: 72px;
    letter-spacing: 1px;
  }
  .ampersand {
    display: block;
    font-size: 56px;
    line-height: 1;
    margin: 14px 0 20px;
  }
  .performer-second {
    font-size: 92px;
    letter-spacing: 2px;
  }
  .event-band {
    position: absolute;
    left: 0;
    top: 1078px;
    width: 100%;
    height: 48px;
    background: var(--red);
    display: flex;
    align-items: center;
    justify-content: center;
  }
  .event-details {
    margin: 0;
    font-family: "Open Sans", sans-serif;
    font-size: 25px;
    color: var(--name-white);
  }
</style>
</head>
<body>
  <main class="flyer">
    <div class="performer-photo" role="img" aria-label="Black and white photo of the two pianists standing side by side in waistcoats, shirts and trousers, shown from the chest down"></div>

    <div class="tagline-band">
      <p class="tagline">A classical concert featuring pianists</p>
    </div>

    <div class="performers">
      <h1 class="performer performer-first">Alan Brisbourne</h1>
      <span class="ampersand">&amp;</span>
      <h1 class="performer performer-second">Ned Farrow</h1>
    </div>

    <div class="event-band">
      <p class="event-details">At Kelwood College on Thursday, 12th June 2014 at&nbsp; 7.30 pm</p>
    </div>
  </main>
</body>
</html>
```